Wealth Management Business Card

We are a professional services consulting firm that specializes in high net worth individuals over $25,000,000, executives C-suite and above, closely held businesses owners, family offices and highly compensated employees.

Our focus is on risk mitigation and tax efficient strategies. Our clients take their risk on themselves and have a proven track record generating wealth. Our directive is to preserve and protect the wealth they’ve already created.

Our company Harbridge Advisory is geared around five directives of asset protection:
1) Legal Structuring
2) Leverage & Financing
3) Risk Management - Asset Protection & Insurance, Trustee Work
4) Asset Management & Investing - Under www.qelvantcapital.com
5) Tax Efficient Strategies

Our Company Mark is a Pentagon with a key in the middle. A pentagon is the most efficient defensive structure. Each point of a pentagon is equal distance front every point . Each side provides support to another and works together, which is the key to our clients success.

Our key colors are blue, black and silver.

We ‘re located in the Pacific Northwest with bi coastal and international clients. We have fewer, higher net worth clients and provide exceptional customer service. We do not do social media.

website is www.harbridgepath.com

Target Market(s)

High End Clients

Contact Information for Business Card

extra thick

Font styles to use
Serif

Requirements
Must have
• Metalic foil for lettering.
Black Background on one side
White Background on the other
Horizontal Format Only
No Rounded corners
Not Marketing sales information on the card.
Nice to have
• imprinted texture on the card
Should not have
• lots of color

```html
<!DOCTYPE html>
<html lang="en">
<head>
<meta charset="utf-8">
<title>Harbridge Advisory – Business Card</title>
<link href="https://fonts.googleapis.com/css2?family=Cinzel:wght@500;600&family=Poppins:wght@400&display=swap" rel="stylesheet">
<style>
  :root {
    --stage: #1b1b1c;
    --stage-light: #2a2a2b;
    --card-black: #0e0e0f;
    --card-white: #ffffff;
    --navy: #152c7a;
    --blue: #1f5fc4;
    --silver: #d4d6d9;
    --silver-dark: #9a9da1;
    --ink: #4a4a4f;
  }
  * { box-sizing: border-box; margin: 0; padding: 0; }
  html, body { width: 1200px; height: 1200px; overflow: hidden; }
  body {
    background: radial-gradient(ellipse at 55% 25%, var(--stage-light), var(--stage) 70%);
    position: relative;
    font-family: "Poppins", sans-serif;
  }
  .card {
    position: absolute;
    left: 170px;
    width: 860px;
    height: 491px;
    border-radius: 14px;
    box-shadow: 0 18px 40px rgba(0,0,0,0.55);
    overflow: hidden;
  }
  .card--front { top: 90px; background: linear-gradient(160deg, #1a1a1b, var(--card-black) 55%); }
  .card--back { top: 620px; background: var(--card-white); }

  .wordmark {
    font-family: "Cinzel", serif;
    font-weight: 600;
    text-align: center;
    line-height: 1;
  }
  .wordmark__top { display: block; font-size: 26px; letter-spacing: 0.42em; margin-bottom: 6px; }
  .wordmark__main { display: block; font-size: 54px; letter-spacing: 0.02em; }

  .card--front .wordmark {
    position: absolute; left: 0; right: 0; top: 190px;
    color: var(--silver);
  }

  .back__brand {
    position: absolute; left: 40px; top: 200px; width: 380px;
    color: var(--navy);
  }
  .back__brand .wordmark__main { font-size: 50px; }
  .back__divider {
    position: absolute; left: 440px; top: 130px;
    width: 2px; height: 230px; background: var(--navy);
  }
  .contact {
    position: absolute; left: 480px; top: 140px; width: 360px;
    color: var(--ink);
  }
  .contact__name {
    font-family: "Cinzel", serif; font-weight: 600;
    color: var(--navy); font-size: 25px; letter-spacing: 0.03em;
    margin-bottom: 14px;
  }
  .contact__row {
    display: flex; align-items: flex-start; gap: 12px;
    font-size: 18px; line-height: 1.5; margin-bottom: 2px;
  }
  .contact__row svg { flex: none; width: 20px; height: 20px; margin-top: 5px; fill: var(--blue); }
  .contact__row--address { margin-top: 10px; }
</style>
</head>
<body>
  <section class="card card--front" aria-label="Card front">
    <div class="wordmark">
      <span class="wordmark__top">Harbridge</span>
      <span class="wordmark__main">ADVISORY</span>
    </div>
  </section>

  <section class="card card--back" aria-label="Card back">
    <div class="wordmark back__brand">
      <span class="wordmark__top">Harbridge</span>
      <span class="wordmark__main">ADVISORY</span>
    </div>
    <div class="back__divider"></div>
    <div class="contact">
      <p class="contact__name">MARCUS ELLERY</p>
      <p class="contact__row">
        <svg viewBox="0 0 24 24" aria-hidden="true"><path d="M6.6 10.8a15.2 15.2 0 0 0 6.6 6.6l2.2-2.2c.3-.3.7-.4 1-.2 1.1.4 2.3.6 3.6.6.6 0 1 .4 1 1V20c0 .6-.4 1-1 1A17 17 0 0 1 3 4c0-.6.4-1 1-1h3.5c.6 0 1 .4 1 1 0 1.3.2 2.5.6 3.6.1.3 0 .7-.2 1z"/></svg>
        (503) 555-0147
      </p>
      <p class="contact__row">
        <svg viewBox="0 0 24 24" aria-hidden="true"><path d="M2 5h20v14H2zm2 2v.5l8 5 8-5V7zm0 2.8V17h16V9.8l-8 5z"/></svg>
        info@harbridgepath.com
      </p>
      <p class="contact__row">
        <svg viewBox="0 0 24 24" aria-hidden="true"><path d="M12 2a10 10 0 1 0 0 20 10 10 0 0 0 0-20zm6.9 6h-2.9a15 15 0 0 0-1.4-3.8A8 8 0 0 1 18.9 8zM12 4c.8 1.2 1.5 2.5 1.9 4h-3.8c.4-1.5 1.1-2.8 1.9-4zM4.3 14a8 8 0 0 1 0-4h3.3a16 16 0 0 0 0 4zm.8 2h2.9c.3 1.4.8 2.7 1.4 3.8A8 8 0 0 1 5.1 16zM8 8H5.1a8 8 0 0 1 4.3-3.8C8.8 5.3 8.3 6.6 8 8zm4 12c-.8-1.2-1.5-2.5-1.9-4h3.8c-.4 1.5-1.1 2.8-1.9 4zm2.3-6H9.7a14 14 0 0 1 0-4h4.6a14 14 0 0 1 0 4zm.3 5.8c.6-1.1 1.1-2.4 1.4-3.8h2.9a8 8 0 0 1-4.3 3.8zm1.8-5.8a16 16 0 0 0 0-4h3.3a8 8 0 0 1 0 4z"/></svg>
        www.harbridgepath.com
      </p>
      <p class="contact__row contact__row--address">
        <svg viewBox="0 0 24 24" aria-hidden="true"><path d="M12 2a7 7 0 0 0-7 7c0 5.2 7 13 7 13s7-7.8 7-13a7 7 0 0 0-7-7zm0 9.5A2.5 2.5 0 1 1 12 6.5a2.5 2.5 0 0 1 0 5z"/></svg>
        212 Alder Crest Rd, Suite 310, Westhaven, OR 97101
      </p>
    </div>
  </section>
</body>
</html>
```